Bluewater Field Logistics

8.5 x 11 flyer one or two sides is fine. This will be used for a trade show. See message for details

Target Market(s)

Refineries and Petrochemical plants

Industry/Entity Type

Oil

```html
<!DOCTYPE html>
<html lang="en">
<head>
<meta charset="utf-8">
<title>Bluewater Field Logistics – Trade Show Flyer</title>
<link rel="stylesheet" href="https://fonts.googleapis.com/css2?family=Montserrat:wght@300;400;500;600;700;800&display=swap">
<style>
  :root {
    --green: #267d52;
    --green-dark: #1f6b45;
    --steel-deep: #1c3250;
    --steel-mid: #3d5a7a;
    --steel-light: #8fa6bc;
    --paper: #ececea;
    --ink: #2b2b2b;
    --black: #0d0d0d;
    --white: #ffffff;
    --backdrop: #d6d6d6;
  }
  * { margin: 0; padding: 0; box-sizing: border-box; }
  html, body {
    width: 1200px; height: 2365px; overflow: hidden;
    background: var(--backdrop);
    font-family: "Montserrat", Arial, sans-serif;
  }
  .flyer-stage {
    position: absolute; left: 50px; top: 335px;
    width: 893px; height: 1375px;
    transform: scale(1.2318); transform-origin: 0 0;
  }
  .flyer {
    position: relative; width: 893px; height: 1375px; overflow: hidden;
    background: var(--paper);
    box-shadow: 4px 6px 14px rgba(0,0,0,.35);
  }
  .hero-photo {
    position: absolute; left: 0; top: 0; width: 893px; height: 565px;
    background:
      linear-gradient(180deg, rgba(28,50,80,.55) 0%, rgba(28,50,80,.25) 45%, rgba(28,50,80,.6) 100%),
      linear-gradient(120deg, var(--steel-light) 0%, var(--steel-mid) 35%, var(--steel-deep) 70%, var(--steel-mid) 100%);
  }
  .shapes { position: absolute; left: 0; top: 0; }
  .brand-name {
    position: absolute; top: 70px; left: 0; width: 100%;
    text-align: center; color: var(--white);
    font-weight: 800; font-size: 40px; letter-spacing: .5px;
  }
  .headline {
    position: absolute; top: 172px; left: 0; width: 100%;
    text-align: center; color: var(--white);
    font-weight: 600; font-size: 50px; letter-spacing: .5px;
  }
  .subhead {
    position: absolute; top: 238px; left: 0; width: 100%;
    text-align: center; color: var(--white);
    font-weight: 400; font-size: 42px; letter-spacing: 9px;
  }
  .tags { position: absolute; top: 300px; left: 124px; display: flex; gap: 10px; }
  .tag {
    height: 50px; padding: 0 20px; display: flex; align-items: center;
    background: var(--green); border: 2px solid var(--white);
    color: var(--white); font-weight: 500; font-size: 26px; white-space: nowrap;
  }
  .what-we-do {
    position: absolute; top: 782px; left: 0; width: 100%;
    text-align: center; color: var(--green);
    font-weight: 600; font-size: 29px;
  }
  .about {
    position: absolute; top: 832px; left: 68px; width: 757px;
    text-align: center; color: var(--ink);
    font-weight: 400; font-size: 15.2px; line-height: 21.6px;
  }
  .materials-band {
    position: absolute; left: 0; top: 990px; width: 893px; height: 266px;
    background: var(--green);
  }
  .materials { position: absolute; top: 26px; list-style: none; }
  .materials li {
    display: flex; align-items: center; height: 33px; white-space: nowrap;
    color: var(--white); font-weight: 500; font-size: 17px;
  }
  .materials svg { width: 18px; height: 18px; margin-right: 10px; flex: none; }
  .col-1 { left: 68px; } .col-2 { left: 319px; } .col-3 { left: 596px; }
  .trusted {
    position: absolute; top: 172px; left: 0; width: 100%;
    text-align: center; color: var(--white);
    font-weight: 600; font-size: 36px;
  }
  .trusted-strip {
    position: absolute; top: 246px; left: 157px; width: 579px; height: 39px;
    background: var(--white); color: var(--green);
    display: flex; align-items: center; justify-content: center;
    font-weight: 500; font-size: 16px; white-space: nowrap; z-index: 2;
  }
  .contact-bar {
    position: absolute; left: 0; top: 1256px; width: 893px; height: 119px;
    background: var(--black); color: var(--white);
  }
  .contact { position: absolute; top: 42px; display: flex; align-items: center; font-size: 27px; font-weight: 500; white-space: nowrap; }
  .contact svg { margin-right: 10px; }
  .phone { left: 92px; } .web { left: 368px; }
  .social { position: absolute; left: 688px; top: 44px; display: flex; gap: 4px; }
</style>
</head>
<body>
<div class="flyer-stage">
  <div class="flyer">
    <div class="hero-photo" role="img" aria-label="Photo of a refinery pipe rack with a worker in a hard hat, seen from below"></div>

    <svg class="shapes" width="893" height="1375" viewBox="0 0 893 1375">
      <defs>
        <linearGradient id="tankFarm" x1="0" y1="0" x2="0" y2="1">
          <stop offset="0" stop-color="#8cb8de"/><stop offset=".5" stop-color="#e4e8ec"/><stop offset="1" stop-color="#5b6d7c"/>
        </linearGradient>
        <linearGradient id="oilPour" x1="0" y1="0" x2="1" y2="1">
          <stop offset="0" stop-color="#eef0f2"/><stop offset=".45" stop-color="#d49a2c"/><stop offset=".7" stop-color="#9a6a18"/><stop offset="1" stop-color="#c8ccd0"/>
        </linearGradient>
        <linearGradient id="column" x1="0" y1="0" x2="1" y2="1">
          <stop offset="0" stop-color="#a9c6e6"/><stop offset=".5" stop-color="#2f5e9c"/><stop offset="1" stop-color="#d7dde4"/>
        </linearGradient>
      </defs>
      <polygon points="231,358 432,563 231,768 30,563" fill="none" stroke="var(--green)" stroke-width="3"/>
      <polygon points="231,383 408,563 231,743 54,563" fill="url(#tankFarm)" role="img" aria-label="Photo of white storage tanks at a waterfront terminal"/>
      <polygon points="773,358 974,563 773,768 572,563" fill="none" stroke="var(--green)" stroke-width="3"/>
      <polygon points="773,383 950,563 773,743 596,563" fill="url(#column)" role="img" aria-label="Photo of a blue distillation column with piping"/>
      <polygon points="488,378 676,563 488,748 300,563" fill="var(--white)" stroke="var(--green)" stroke-width="10"/>
      <polygon points="488,398 656,563 488,728 320,563" fill="url(#oilPour)" role="img" aria-label="Photo of golden oil pouring from a bottle neck"/>
    </svg>

    <div class="brand-name">Bluewater Field Logistics</div>
    <h1 class="headline">YOUR STRATEGIC PARTNER</h1>
    <p class="subhead">For Productive Solutions</p>
    <div class="tags">
      <span class="tag">Byproducts</span>
      <span class="tag">Coproducts</span>
      <span class="tag">Process Residuals</span>
    </div>

    <h2 class="what-we-do">WHAT WE DO</h2>
    <p class="about">Bluewater Field Logistics utilizes a multi-faceted approach by supporting various manufacturers, refineries, blender/packagers and distributors by purchasing residual by-products, co-products, bottoms, off spec or out of date and surplus material. We truly pride ourselves on our ability to source your residual materials as a feedstock into a secondary market; thereby improving your bottom line and improving the sustainability of our environment. In addition, we also review waste material for reuse or recycle. Whether truck, rail or barge, Bluewater is here to meet your needs.</p>

    <section class="materials-band">
      <ul class="materials col-1">
        <li><svg viewBox="0 0 18 18"><path d="M15 8v8H2V3h9" fill="none" stroke="#fff" stroke-width="1.6"/><path d="M5 8l3 3 8-8" fill="none" stroke="#fff" stroke-width="1.6"/></svg>Alcohols</li>
        <li><svg viewBox="0 0 18 18"><path d="M15 8v8H2V3h9" fill="none" stroke="#fff" stroke-width="1.6"/><path d="M5 8l3 3 8-8" fill="none" stroke="#fff" stroke-width="1.6"/></svg>Asphalt Flux</li>
        <li><svg viewBox="0 0 18 18"><path d="M15 8v8H2V3h9" fill="none" stroke="#fff" stroke-width="1.6"/><path d="M5 8l3 3 8-8" fill="none" stroke="#fff" stroke-width="1.6"/></svg>Bitumen</li>
        <li><svg viewBox="0 0 18 18"><path d="M15 8v8H2V3h9" fill="none" stroke="#fff" stroke-width="1.6"/><path d="M5 8l3 3 8-8" fill="none" stroke="#fff" stroke-width="1.6"/></svg>Crude Oil</li>
      </ul>
      <ul class="materials col-2">
        <li><svg viewBox="0 0 18 18"><path d="M15 8v8H2V3h9" fill="none" stroke="#fff" stroke-width="1.6"/><path d="M5 8l3 3 8-8" fill="none" stroke="#fff" stroke-width="1.6"/></svg>Distillation Residue</li>
        <li><svg viewBox="0 0 18 18"><path d="M15 8v8H2V3h9" fill="none" stroke="#fff" stroke-width="1.6"/><path d="M5 8l3 3 8-8" fill="none" stroke="#fff" stroke-width="1.6"/></svg>Distressed Material</li>
        <li><svg viewBox="0 0 18 18"><path d="M15 8v8H2V3h9" fill="none" stroke="#fff" stroke-width="1.6"/><path d="M5 8l3 3 8-8" fill="none" stroke="#fff" stroke-width="1.6"/></svg>Fuels</li>
        <li><svg viewBox="0 0 18 18"><path d="M15 8v8H2V3h9" fill="none" stroke="#fff" stroke-width="1.6"/><path d="M5 8l3 3 8-8" fill="none" stroke="#fff" stroke-width="1.6"/></svg>Glycols</li>
      </ul>
      <ul class="materials col-3">
        <li><svg viewBox="0 0 18 18"><path d="M15 8v8H2V3h9" fill="none" stroke="#fff" stroke-width="1.6"/><path d="M5 8l3 3 8-8" fill="none" stroke="#fff" stroke-width="1.6"/></svg>Petroleum Hydrocarbons</li>
        <li><svg viewBox="0 0 18 18"><path d="M15 8v8H2V3h9" fill="none" stroke="#fff" stroke-width="1.6"/><path d="M5 8l3 3 8-8" fill="none" stroke="#fff" stroke-width="1.6"/></svg>Solvents</li>
        <li><svg viewBox="0 0 18 18"><path d="M15 8v8H2V3h9" fill="none" stroke="#fff" stroke-width="1.6"/><path d="M5 8l3 3 8-8" fill="none" stroke="#fff" stroke-width="1.6"/></svg>Tank Bottoms</li>
        <li><svg viewBox="0 0 18 18"><path d="M15 8v8H2V3h9" fill="none" stroke="#fff" stroke-width="1.6"/><path d="M5 8l3 3 8-8" fill="none" stroke="#fff" stroke-width="1.6"/></svg>And More!</li>
      </ul>
      <p class="trusted">Your Trusted Partner for 26 Years!</p>
      <p class="trusted-strip">Procurement of Process Residuals and Off-Spec Material Worldwide</p>
    </section>

    <footer class="contact-bar">
      <div class="contact phone">
        <svg width="22" height="22" viewBox="0 0 24 24"><path d="M6 3l3 4-2 2c1 3 4 6 7 7l2-2 4 3-2 4C10 21 3 14 3 5z" fill="none" stroke="#fff" stroke-width="2"/></svg>
        843-555-0142
      </div>
      <div class="contact web">
        <svg width="22" height="22" viewBox="0 0 24 24" fill="none" stroke="#fff" stroke-width="1.6"><circle cx="12" cy="12" r="10"/><ellipse cx="12" cy="12" rx="4.5" ry="10"/><path d="M2 12h20M4 7h16M4 17h16"/></svg>
        www.bwf-log.com
      </div>
      <div class="social">
        <svg width="34" height="34" viewBox="0 0 34 34"><rect x="7" y="7" width="20" height="20" transform="rotate(45 17 17)" fill="#fff"/></svg>
        <svg width="34" height="34" viewBox="0 0 34 34"><rect x="7" y="7" width="20" height="20" transform="rotate(45 17 17)" fill="#fff"/></svg>
        <svg width="34" height="34" viewBox="0 0 34 34"><rect x="7" y="7" width="20" height="20" transform="rotate(45 17 17)" fill="#fff"/></svg>
      </div>
    </footer>
  </div>
</div>
</body>
</html>
```